IT support company needs Banner Ad for the top of their quote layout template

We need a banner Ad for the top of our for quote layout template so it is sent out on all our quotes

The banner size must be 827 x 100 pixels - anything larger than 60 KB can cause upload time issues

We have attached our logo and examples of the quote page to see how it looks in the context of the whole page.

Essential elements of the banner
- Must have our logo but this can be changed to be different colours if it makes the design work better i.e. Tidal Grove could be all in white

Colours
- Can use all of our standard colours - Orange, Black, Grey and White

Images
- As a premium IT support company we deal with people and technology so would like to see both of these Incorporated into the banner i.e. people using technology These images could be watermarked or one colour effect.

Look and Feel
- Professional, friendly, people, technology, premium

Target Market
Small business owners and managers

Industry/Entity Type

It Company

```html
<!DOCTYPE html>
<html lang="en">
<head>
<meta charset="utf-8">
<title>Tidal Grove – Quote Banner</title>
<link href="https://fonts.googleapis.com/css2?family=Lato:wght@400;700;900&display=swap" rel="stylesheet">
<style>
  :root {
    --page: #ffffff;
    --ink: #17181b;
    --orange: #ef8a2c;
    --white: #ffffff;
    --blue: #2a7dc4;
    --photo-light: #eef1f4;
    --photo-mid: #c9d2dc;
    --photo-deep: #8a98a8;
  }
  html, body {
    margin: 0;
    width: 1200px;
    height: 1200px;
    overflow: hidden;
    background: var(--page);
  }
  .banner {
    position: absolute;
    left: 140px;
    top: 489px;
    width: 919px;
    height: 110px;
    overflow: hidden;
    font-family: "Lato", sans-serif;
  }
  .banner__photo {
    position: absolute;
    inset: 0;
    background: linear-gradient(100deg, var(--photo-deep) 0%, var(--photo-mid) 30%, var(--photo-light) 50%, var(--photo-mid) 65%, var(--photo-light) 80%, var(--photo-mid) 100%);
  }
  .banner__shapes {
    position: absolute;
    inset: 0;
  }
  .banner__headline {
    position: absolute;
    left: 10px;
    top: 28px;
    margin: 0;
    color: var(--white);
    font-weight: 900;
    font-size: 21px;
    line-height: 26px;
    letter-spacing: -0.3px;
    text-transform: uppercase;
  }
  .banner__offer {
    position: absolute;
    left: 768px;
    top: 14px;
    margin: 0;
    color: var(--white);
    font-weight: 400;
    font-size: 21px;
    line-height: 27px;
    letter-spacing: -0.2px;
  }
  .banner__cta {
    position: absolute;
    left: 777px;
    top: 73px;
    width: 106px;
    height: 26px;
    background: var(--blue);
    color: var(--white);
    font-weight: 900;
    font-size: 11.5px;
    display: flex;
    align-items: center;
    justify-content: center;
    gap: 6px;
    text-decoration: none;
    letter-spacing: -0.2px;
  }
  .banner__brand {
    position: absolute;
    left: 384px;
    top: 89px;
    color: var(--ink);
    font-weight: 900;
    font-size: 14px;
    letter-spacing: -0.2px;
    text-transform: uppercase;
  }
</style>
</head>
<body>
  <section class="banner">
    <div class="banner__photo" role="img" aria-label="Office worker holding a tablet in front of computer monitors by a bright window"></div>
    <svg class="banner__shapes" width="919" height="110" viewBox="0 0 919 110" aria-hidden="true">
      <polygon points="0,0 260,0 156,110 0,110" fill="var(--ink)"/>
      <polygon points="260,0 304,0 242,58 206,58" fill="var(--orange)"/>
      <polygon points="708,0 768,0 722,58 700,40" fill="var(--orange)"/>
      <polygon points="768,0 919,0 919,110 672,110" fill="var(--ink)"/>
    </svg>
    <h1 class="banner__headline">A big headline<br>will go here</h1>
    <p class="banner__offer">A small text<br>will go here</p>
    <a class="banner__cta" href="#">CLICK HERE
      <svg width="10" height="9" viewBox="0 0 10 9" aria-hidden="true"><polygon points="0,3 5,3 5,0 10,4.5 5,9 5,6 0,6" fill="var(--orange)"/></svg>
    </a>
    <span class="banner__brand">Tidal Grove</span>
  </section>
</body>
</html>
```